GetShelf screenshots

We need an GetShelf screenshot design for our app. The design should be for the all Nuvadexes and Korvis. Please see attached for sample (Nuvadex & Korvi) and images. Use the website www.plomvex.com for color guidance.

```html
<!DOCTYPE html>
<html lang="en">
<head>
<meta charset="utf-8">
<title>Plomvex – GetShelf screenshots</title>
<link href="https://fonts.googleapis.com/css2?family=Plus+Jakarta+Sans:wght@400;600;800&family=Roboto+Mono:wght@400&display=swap" rel="stylesheet">
<style>
:root{
  --paper:#f7f8fc;
  --navy:#2b2850;
  --navy-2:#38345f;
  --navy-3:#46426e;
  --blue:#2f6fc4;
  --blue-line:#3a7fd6;
  --ink:#2b2850;
  --screen:#ffffff;
  --rule:#eceef4;
  --teal:#3fd0b8;
  --bar-blue:#3f6fb5;
  --bar-red:#6b1a1f;
  --up:#39d353;
  --down:#ff2a2a;
  --text:#222;
  --muted:#8d8aa8;
}
*{box-sizing:border-box;margin:0;padding:0}
html,body{width:1200px;height:389px;overflow:hidden;background:var(--paper)}
body{font-family:"Plus Jakarta Sans",sans-serif;color:var(--ink)}
.canvas{position:relative;width:1200px;height:389px;overflow:hidden;background:var(--paper)}
.backdrop{position:absolute;inset:0}
.heading{position:absolute;font-weight:800;font-size:15.5px;line-height:19px;color:var(--ink);letter-spacing:-.1px}
.heading.center{text-align:center}

/* dashboard */
.dashboard{position:absolute;left:108px;top:118px;width:280px;height:200px;background:var(--navy-2);border-radius:8px;padding:8px;display:grid;grid-template-columns:repeat(3,1fr);grid-template-rows:repeat(2,1fr);gap:6px}
.tile{background:var(--navy-3);border-radius:4px;padding:6px;position:relative;color:#fff}
.tile-label{font-size:7px;font-weight:800;color:#f0d24a;letter-spacing:.3px}
.tile-value{font-size:12px;font-weight:600;margin-top:3px}
.tile-note{font-size:4.5px;color:var(--muted);margin-top:2px}
.tile-chip{position:absolute;right:5px;top:5px;font-size:4.5px;padding:1px 3px;border-radius:3px;color:#fff;background:var(--down)}
.tile-chip.up{background:var(--up)}
.tile-bar{position:absolute;left:6px;right:6px;bottom:8px;height:30px;background:#55507c;border-radius:2px}
.tile-bar i{position:absolute;left:0;bottom:0;width:100%;background:var(--blue)}
.tile-bar i.red{background:#8a2430}

/* screens */
.screen{position:absolute;top:100px;width:118px;height:252px;background:var(--screen);border-radius:9px;overflow:hidden;font-size:4px;color:var(--text)}
.screen-top{background:var(--navy);height:28px;color:#fff;position:relative}
.status{position:absolute;left:8px;top:5px;font-size:4.6px}
.status-icons{position:absolute;right:8px;top:6px;width:16px;height:3px;background:#fff;border-radius:1px;opacity:.85}
.title{position:absolute;left:0;right:0;top:17px;text-align:center;font-size:4.6px;letter-spacing:.2px}
.back{position:absolute;left:6px;top:15px;width:5px;height:5px;border-left:1px solid #fff;border-bottom:1px solid #fff;transform:rotate(45deg)}
.screen-nav{position:absolute;left:0;right:0;bottom:0;height:26px;background:var(--navy);color:#fff;display:flex;justify-content:space-around;padding-top:6px;font-size:4.2px}
.screen-nav .on{color:var(--teal)}
.screen-nav::after{content:"";position:absolute;bottom:4px;left:38%;width:24%;height:1.2px;background:#fff;border-radius:1px}

/* trend */
.trend-all{position:absolute;left:8px;top:38px;color:var(--teal);font-size:5.5px;font-weight:600}
.trend-rows{position:absolute;left:6px;top:52px;width:108px}
.trend-row{height:13px;display:flex;align-items:center;font-size:4.2px;font-weight:600}
.trend-row span:first-child{width:12px;text-align:right;margin-right:3px}
.trend-bar{height:6px}
.trend-bar.blue{background:var(--bar-blue)}
.trend-bar.red{background:var(--bar-red)}
.trend-amt{margin-left:2px;font-size:4px}
.trend-axis{position:absolute;left:21px;top:54px;width:0;height:155px;border-left:.5px solid #bbb}
.trend-ticks{position:absolute;left:17px;top:212px;width:96px;display:flex;justify-content:space-between;font-size:3.8px;font-weight:600}

/* tables */
.table{position:absolute;left:0;right:0;top:28px}
.table-head,.table-row{display:grid;align-items:center;padding:0 4px}
.table-head{height:11px;font-size:3px;font-weight:600;border-bottom:.5px solid var(--rule)}
.table-row{border-bottom:.5px solid var(--rule);font-size:3.3px;line-height:4.4px}
.contractors .table-head,.contractors .table-row{grid-template-columns:22px 26px 17px 20px 1fr}
.contractors .table-row{height:20.5px}
.agencies .table-head,.agencies .table-row{grid-template-columns:46px 20px 22px 1fr}
.agencies .table-row{height:16.7px}
.num{text-align:center}
.badge{justify-self:end;font-size:2.6px;color:#fff;padding:1px 2px;border-radius:1.5px;min-width:17px;text-align:center}
.badge.up{background:var(--up);color:#0c3d12}
.badge.down{background:var(--down)}

/* brand */
.brand{position:absolute;left:27px;top:328px;color:#fff}
.brand-name{font-size:22px;font-weight:400;letter-spacing:.5px}
.brand-tag{font-family:"Roboto Mono",monospace;font-size:3.8px;margin-top:2px}
</style>
</head>
<body>
<main class="canvas">
  <svg class="backdrop" width="1200" height="389" viewBox="0 0 1200 389" aria-hidden="true">
    <path fill="var(--blue)" d="M0,96 C120,110 230,150 320,140 C430,128 520,118 610,128 C700,140 760,190 880,186 C990,182 1090,170 1200,150 L1200,389 L0,389 Z"/>
    <path fill="var(--navy)" d="M0,104 C110,160 220,180 330,170 C450,158 520,160 600,190 C680,225 700,250 780,240 C880,228 900,270 1000,300 C1080,320 1150,300 1200,285 L1200,389 L0,389 Z"/>
    <g fill="none" stroke-width="1">
      <path stroke="var(--ink)" d="M386,58v12M380,64h12"/>
      <circle stroke="var(--ink)" cx="402" cy="85" r="8.5"/>
      <path stroke="var(--ink)" d="M680,136h16"/>
      <circle stroke="var(--blue-line)" cx="471" cy="230" r="21"/>
      <path stroke="var(--blue-line)" d="M498,302v22M487,313h22"/>
      <path stroke="var(--blue-line)" d="M63,300v14M56,307h14"/>
      <circle stroke="var(--blue-line)" cx="95" cy="329" r="6.5"/>
      <path stroke="var(--blue-line)" d="M108,358h16M128,358h16M148,358h16"/>
      <path stroke="var(--blue-line)" d="M738,171v16M730,179h16"/>
      <circle stroke="var(--ink)" cx="928" cy="108" r="8.5"/>
      <path stroke="var(--ink)" d="M895,74h16"/>
      <circle stroke="var(--blue-line)" cx="803" cy="335" r="31"/>
      <path stroke="var(--ink)" d="M1162,75v12M1156,81h12"/>
      <circle stroke="var(--ink)" cx="1175" cy="101" r="6.5"/>
      <path stroke="var(--blue-line)" d="M967,315h16M987,315h16M1007,315h8"/>
    </g>
  </svg>

  <h1 class="heading" style="left:27px;top:46px">US Government Finances<br>at your fingertips</h1>
  <h2 class="heading" style="left:522px;top:46px">Track monthly trends</h2>
  <h2 class="heading center" style="left:740px;top:29px;width:200px">Contractor spend by<br>department</h2>
  <h2 class="heading" style="left:1010px;top:46px">Sub-agency spend</h2>

  <section class="dashboard" aria-label="Finance dashboard">
    <div class="tile"><div class="tile-label">REVENUE</div><div class="tile-value">$245.5B</div><div class="tile-note">Updated: Oct 31</div><span class="tile-chip up">9.54%</span><div class="tile-bar"><i style="height:60%"></i></div></div>
    <div class="tile"><div class="tile-label">EXPENSES</div><div class="tile-value">$380.0B</div><div class="tile-note">Updated: Oct 31</div><span class="tile-chip">74.11B</span><div class="tile-bar"><i style="height:75%"></i></div></div>
    <div class="tile"><div class="tile-label">DEFICIT</div><div class="tile-value">-$134.5B</div><div class="tile-note">Updated: Oct 31</div><span class="tile-chip">65.1B</span><div class="tile-bar"><i class="red" style="height:45%"></i></div></div>
    <div class="tile"><div class="tile-label">CASH</div><div class="tile-value">$374.2B</div><div class="tile-note">Updated: Nov 26</div><span class="tile-chip up">4.88B</span><div class="tile-bar"><i style="height:50%"></i></div></div>
    <div class="tile"><div class="tile-label">DEBT</div><div class="tile-value">$23.09T</div><div class="tile-note">Updated: Nov 26</div><span class="tile-chip">1.27T</span><div class="tile-bar"><i class="red" style="height:80%"></i></div></div>
    <div class="tile"><div class="tile-label">DEBT PER TAXPAYER</div><div class="tile-value">$163.7k</div><div class="tile-note">Updated: Nov 26</div><span class="tile-chip">9.4k</span><div class="tile-bar"><i class="red" style="height:70%"></i></div></div>
  </section>

  <section class="screen" style="left:540px" aria-label="Monthly trend screen">
    <div class="screen-top"><span class="status">2:28</span><span class="status-icons"></span><span class="back"></span><div class="title">GOVERNMENTHOLDINGS</div></div>
    <div class="trend-all">ALL</div>
    <div class="trend-axis"></div>
    <div class="trend-rows">
      <div class="trend-row"><span>Oct</span><span class="trend-bar blue" style="width:76px"></span><span class="trend-amt">116.8B</span></div>
      <div class="trend-row"><span>Nov</span><span class="trend-bar red" style="width:37px"></span><span class="trend-amt">-56.32B</span></div>
      <div class="trend-row"><span>Dec</span></div>
      <div class="trend-row"><span>Jan</span></div>
      <div class="trend-row"><span>Feb</span></div>
      <div class="trend-row"><span>Mar</span></div>
      <div class="trend-row"><span>Apr</span></div>
      <div class="trend-row"><span>May</span></div>
      <div class="trend-row"><span>Jun</span></div>
      <div class="trend-row"><span>Jul</span></div>
      <div class="trend-row"><span>Aug</span></div>
      <div class="trend-row"><span>Sep</span></div>
    </div>
    <div class="trend-ticks"><span>0</span><span>29.20B</span><span>58.39B</span><span>87.59B</span><span>116.8B</span></div>
    <nav class="screen-nav"><span>About</span><span class="on">Trend</span></nav>
  </section>

  <section class="screen" style="left:782px" aria-label="Contractor spend screen">
    <div class="screen-top"><span class="status">2:29</span><span class="status-icons"></span><span class="back"></span><div class="title">DEPT. OF HHS</div></div>
    <div class="table contractors">
      <div class="table-head"><span>Contractor</span><span>Prod./service</span><span class="num">$LY</span><span class="num">$total YTD</span><span class="num">$Var</span></div>
      <div class="table-row"><span>VELTRA &amp; CO. INC.</span><span>BIOLOGICAL PRODUCT</span><span class="num">264.0T</span><span class="num">606.7T</span><span class="badge up">342.8T</span></div>
      <div class="table-row"><span>QUORANE INC.</span><span>PHARMACEUTICAL</span><span class="num">177.6T</span><span class="num">297.9T</span><span class="badge up">120.3T</span></div>
      <div class="table-row"><span>HARLOW BRISK PLC</span><span>MEDICINAL AND BOTANICA...</span><span class="num">177.1T</span><span class="num">221.4T</span><span class="badge up">44.25T</span></div>
      <div class="table-row"><span>DELMARA</span><span>MEDICINAL AND BOTANICA...</span><span class="num">114.1T</span><span class="num">157.5T</span><span class="badge up">43.38T</span></div>
      <div class="table-row"><span>TRISTAN RESEARCH INSTITUTE</span><span>ALL OTHER PROFESSIONAL</span><span class="num">43.98T</span><span class="num">33.11T</span><span class="badge down">10.87T</span></div>
      <div class="table-row"><span>CORVANTA INC.</span><span>OTHER SCIENTIFIC AND TECH</span><span class="num">52.77T</span><span class="num">24.14T</span><span class="badge down">28.63T</span></div>
      <div class="table-row"><span>BRENNICK DATA ENTERPR...</span><span>COMPUTER AND OFFICE</span><span class="num">19.87T</span><span class="num">20.07T</span><span class="badge up">197.1B</span></div>
      <div class="table-row"><span>PRISM CARE RESOURCES</span><span>ALL OTHER MISCELLANEOUS</span><span class="num">3.402T</span><span class="num">18.56T</span><span class="badge up">15.16T</span></div>
      <div class="table-row"><span>ELM HOLLOW ASSOC. UNIV.</span><span>ALL OTHER PROFESSIONAL</span><span class="num">15.75T</span><span class="num">15.99T</span><span class="badge up">241.4B</span></div>
    </div>
    <nav class="screen-nav"><span>About</span><span class="on">Contractors</span><span>Details</span><span>Trend</span></nav>
  </section>

  <section class="screen" style="left:1018px" aria-label="Sub-agency spend screen">
    <div class="screen-top"><span class="status">2:29</span><span class="status-icons"></span><span class="back"></span><div class="title">DEPT. OF HHS</div></div>
    <div class="table agencies">
      <div class="table-head"><span>Sub-agency</span><span class="num">$LY</span><span class="num">$total YTD</span><span class="num">$Var</span></div>
      <div class="table-row"><span>Medicare/Medicaid</span><span class="num">124.9B</span><span class="num">135.1B</span><span class="badge down">10.23B</span></div>
      <div class="table-row"><span>Children/Families</span><span class="num">4.265B</span><span class="num">4.847B</span><span class="badge down">582.0M</span></div>
      <div class="table-row"><span>Institutes of Health</span><span class="num">2.629B</span><span class="num">3.179B</span><span class="badge down">550.0M</span></div>
      <div class="table-row"><span>Health Resources</span><span class="num">935.0M</span><span class="num">1.077B</span><span class="badge down">142.0M</span></div>
      <div class="table-row"><span>Disease Control</span><span class="num">596.0M</span><span class="num">706.0M</span><span class="badge down">110.0M</span></div>
      <div class="table-row"><span>Subst. Abuse/ Ment. Health</span><span class="num">331.0M</span><span class="num">458.0M</span><span class="badge down">127.0M</span></div>
      <div class="table-row"><span>Indian Health</span><span class="num">345.0M</span><span class="num">393.0M</span><span class="badge down">48.00M</span></div>
      <div class="table-row"><span>Depart. Management</span><span class="num">238.0M</span><span class="num">308.0M</span><span class="badge down">70.00M</span></div>
      <div class="table-row"><span>Community Living</span><span class="num">125.0M</span><span class="num">172.0M</span><span class="badge down">47.00M</span></div>
      <div class="table-row"><span>Other</span><span class="num">-165.0M</span><span class="num">88.00M</span><span class="badge down">253.0M</span></div>
      <div class="table-row"><span>Healthcare Research</span><span class="num">25.00M</span><span class="num">29.00M</span><span class="badge down">4.000M</span></div>
    </div>
    <nav class="screen-nav"><span>About</span><span>Contractors</span><span class="on">Details</span><span>Trend</span></nav>
  </section>

  <div class="brand">
    <div class="brand-name">Plomvex</div>
    <div class="brand-tag">Strategic Financial Planner</div>
  </div>
</main>
</body>
</html>
```